Sticker Design

Wanting business name across the bottom of car doors, please see attached. looking for something simple and require asap. Happy for black and white simple colouring.

Thank you
Dane Morvill

```html
<!DOCTYPE html>
<html lang="en">
<head>
<meta charset="utf-8">
<title>DRM Field Service and Logistics – Door Sticker</title>
<link rel="stylesheet" href="https://fonts.googleapis.com/css2?family=Orbitron:wght@500;700;900&display=swap">
<style>
  :root {
    --backdrop: #b8b8b8;
    --sticker-black: #0d0d0d;
    --sticker-white: #ffffff;
  }
  * { margin: 0; padding: 0; box-sizing: border-box; }
  html, body {
    width: 1200px;
    height: 1200px;
    overflow: hidden;
    background: var(--backdrop);
  }
  .canvas {
    position: relative;
    width: 1200px;
    height: 1200px;
    background: var(--backdrop);
  }
  .door-sticker {
    position: absolute;
    left: 162px;
    top: 556px;
    width: 848px;
    height: 88px;
  }
  .pinstripe {
    position: absolute;
    left: 0;
    top: 0;
    width: 100%;
    height: 7px;
    background: var(--sticker-black);
  }
  .name-band {
    position: absolute;
    left: 0;
    top: 14px;
    width: 100%;
    height: 74px;
    background: var(--sticker-black);
    color: var(--sticker-white);
    font-family: "Orbitron", sans-serif;
  }
  .business-name {
    position: absolute;
    left: 120px;
    top: 6px;
    font-weight: 900;
    font-size: 56px;
    line-height: 62px;
    letter-spacing: 2px;
  }
  .tagline {
    position: absolute;
    left: 361px;
    top: 6px;
    font-weight: 700;
    font-size: 17px;
    line-height: 22px;
    letter-spacing: 1.6px;
    text-transform: uppercase;
    white-space: nowrap;
  }
  .phone {
    position: absolute;
    left: 411px;
    top: 34px;
    display: flex;
    align-items: center;
    gap: 4px;
    font-weight: 900;
    font-size: 27px;
    line-height: 32px;
    letter-spacing: 1.5px;
    white-space: nowrap;
  }
  .phone-icon { width: 29px; height: 29px; flex: none; }
</style>
</head>
<body>
<main class="canvas">
  <section class="door-sticker">
    <div class="pinstripe"></div>
    <div class="name-band">
      <span class="business-name">DRM</span>
      <span class="tagline">Field Service and Logistics</span>
      <span class="phone">
        <svg class="phone-icon" viewBox="0 0 30 30" aria-hidden="true">
          <circle cx="15" cy="15" r="14" fill="#ffffff"/>
          <path d="M10.2 7.2c.8-.5 1.7-.3 2.2.5l1.6 2.6c.4.7.3 1.6-.3 2.1l-1.3 1c.9 2 2.4 3.6 4.3 4.6l1.1-1.2c.6-.6 1.5-.7 2.1-.2l2.5 1.8c.7.5.9 1.5.4 2.2l-1 1.4c-.7 1-2 1.4-3.1 1-5.2-1.8-9-5.8-10.5-11.1-.3-1.2.1-2.4 1.1-3.1z" fill="#0d0d0d"/>
        </svg>
        040-217-3648
      </span>
    </div>
  </section>
</main>
</body>
</html>
```